Business card design Needed for new logo / Construction business, home extensions and new builds

We need a business card design using our new logo files which i will attach to this project :)

We are a small construction business specialising in home extensions, new builds and property development. We are very ambitious and would appreciate professional and elegant designs for our new business card.

Very serious about using the services on BriefNest and recently acquired our new logo from here :)

Please get involved, i will feedback when i can as i am very busy but can respond daily, thanks

Target Market(s)

People that want to build onto their houses, new building developments or adding too their existing property

Industry/Entity Type

Construction

Contact Information for Business Card

Hollin Marsh Construction, Tobias Renwick (Managing Director), Tel 07822200444, email - info@hollin-marsh, www.hollin-marsh.co.uk

Colors

Designer to choose colors to be used in the design.

Requirements
Must have
• I like a deep grey on the back please. A lot of you have provided black from and back, try mixing things up a little. The black looks cool 😎 Thanks

```html
<!DOCTYPE html>
<html lang="en">
<head>
<meta charset="utf-8">
<title>Hollin Marsh Construction – Business Card</title>
<link rel="stylesheet" href="https://fonts.googleapis.com/css2?family=Montserrat:wght@400;500;600&display=swap">
<style>
  :root {
    --canvas: #474747;
    --card-black: #0b0b0b;
    --card-grey: #262626;
    --card-grey-light: #2f2f2f;
    --card-white: #ffffff;
    --gold: #d4a22a;
    --gold-soft: #e3b84a;
    --text-light: #f2f2f2;
  }
  * { margin: 0; padding: 0; box-sizing: border-box; }
  html, body {
    width: 1200px; height: 1200px; overflow: hidden;
    background: var(--canvas);
    font-family: "Montserrat", sans-serif;
  }
  .stage {
    width: 1200px; height: 1200px;
    display: flex; flex-direction: column; align-items: center; justify-content: center;
    gap: 70px;
  }
  .card {
    position: relative;
    width: 770px; height: 440px;
    border-radius: 30px;
    overflow: hidden;
    box-shadow: 0 18px 40px rgba(0,0,0,0.45);
  }
  .card-front { background: var(--card-white); }
  .front-shapes { position: absolute; inset: 0; }
  .contact-block {
    position: absolute; left: 70px; top: 150px;
    color: var(--text-light);
  }
  .person {
    border-left: 5px solid var(--gold);
    padding-left: 14px;
    margin-bottom: 26px;
  }
  .person-name {
    color: var(--gold-soft);
    font-weight: 600; font-size: 27px; letter-spacing: 0.5px;
    line-height: 1.1;
  }
  .person-role {
    font-size: 15px; font-weight: 500; letter-spacing: 0.8px; margin-top: 4px;
  }
  .contact-list { list-style: none; }
  .contact-list li {
    display: flex; align-items: center; gap: 14px;
    font-size: 19px; margin-bottom: 12px; padding-left: 20px;
  }
  .contact-list svg { width: 22px; height: 22px; flex: none; }
  .wordmark {
    display: flex; align-items: center; gap: 14px;
    color: var(--gold);
    font-weight: 500; letter-spacing: 2px; text-transform: uppercase;
    white-space: nowrap;
  }
  .wordmark-square { background: var(--gold); flex: none; }
  .front-brand {
    position: absolute; left: 500px; right: 20px; top: 0; bottom: 0;
    display: flex; align-items: center; justify-content: center;
    padding-bottom: 60px;
  }
  .card-front .wordmark { font-size: 20px; line-height: 1.4; }
  .card-front .wordmark-square { width: 16px; height: 16px; }
  .card-back {
    background: radial-gradient(ellipse at 50% 40%, var(--card-grey-light) 0%, var(--card-grey) 70%);
    display: flex; align-items: center; justify-content: center;
  }
  .card-back .wordmark { font-size: 32px; }
  .card-back .wordmark-square { width: 22px; height: 22px; }
</style>
</head>
<body>
<main class="stage">
  <section class="card card-front" aria-label="Business card front">
    <svg class="front-shapes" viewBox="0 0 770 440" preserveAspectRatio="none" aria-hidden="true">
      <polygon points="0,0 215,0 420,110 470,440 0,440" fill="var(--card-black)"/>
      <polyline points="232,0 437,110 487,440" fill="none" stroke="var(--gold)" stroke-width="5"/>
    </svg>
    <div class="contact-block">
      <div class="person">
        <div class="person-name">TOBIAS RENWICK</div>
        <div class="person-role">MANAGING DIRECTOR</div>
      </div>
      <ul class="contact-list">
        <li>
          <svg viewBox="0 0 24 24" aria-hidden="true"><path fill="var(--gold)" d="M6.6 10.8a15.2 15.2 0 0 0 6.6 6.6l2.2-2.2c.3-.3.7-.4 1-.2 1.1.4 2.3.6 3.6.6.6 0 1 .4 1 1V20c0 .6-.4 1-1 1A17 17 0 0 1 3 4c0-.6.4-1 1-1h3.5c.6 0 1 .4 1 1 0 1.3.2 2.5.6 3.6.1.3 0 .7-.2 1z"/></svg>
          +44 7822 200 444
        </li>
        <li>
          <svg viewBox="0 0 24 24" aria-hidden="true"><rect x="2" y="5" width="20" height="14" fill="none" stroke="var(--gold)" stroke-width="2"/><path d="M2 5l10 8 10-8" fill="none" stroke="var(--gold)" stroke-width="2"/></svg>
          info@hollin-marsh.co.uk
        </li>
        <li>
          <svg viewBox="0 0 24 24" aria-hidden="true"><g fill="none" stroke="var(--gold)" stroke-width="1.8"><circle cx="12" cy="12" r="9.5"/><ellipse cx="12" cy="12" rx="4.5" ry="9.5"/><path d="M2.5 12h19M4 7h16M4 17h16"/></g></svg>
          www.hollin-marsh.co.uk
        </li>
      </ul>
    </div>
    <div class="front-brand">
      <div class="wordmark"><span class="wordmark-square"></span><span>Hollin Marsh<br>Construction</span></div>
    </div>
  </section>

  <section class="card card-back" aria-label="Business card back">
    <div class="wordmark"><span class="wordmark-square"></span>Hollin Marsh Construction</div>
  </section>
</main>
</body>
</html>
```